Silver Reed Harbour Seniors Fairway Festival 2107

I would like a design for an A4 Event Flyer.

This is a golf event for Senior ladies and gentlemen. I would like the design to appeal to an older age group.

I would like somewhere on the flyer a golf ball image with the following details inside "Please put me on your notice board"

The information on the Flyer is as follows
- (Title - Silver reed Harbour Seniors Fairway Festival 2017)
- Date 16th of October to 20th of October
- Over 55 years of age
- We invite our fellow Veteran Ladies and Gentlemen to play a unique 54 hole stableford event at three fantastic Golf Courses, and finish the week at Brindle Golf club with a 2BBB Medley.
- Insert schedule that is attached in PDF. They layout can be changed.

- For entry form and details
Contact: Brindle Proshop on 02 63918204 or email admin@brindlewexmoorgolf.com.au

I have attached 4 golf course images. This is a photo of each course. Could I please get these added to the flyer.

Target Market(s)

seniors

Industry/Entity Type

Golf Course

Requirements
Must have
• All information provided

```html
<!DOCTYPE html>
<html lang="en">
<head>
<meta charset="utf-8">
<title>Silver Reed Harbour Seniors Fairway Festival 2017</title>
<link href="https://fonts.googleapis.com/css2?family=Bebas+Neue&family=Lato:wght@400;700&display=swap" rel="stylesheet">
<style>
  :root {
    --page-bg: #e9e6e1;
    --paper: #ffffff;
    --green-dark: #0d4a25;
    --green: #2a8f4e;
    --green-mid: #1f7a3f;
    --lime: #c9d43b;
    --ink: #1f2a22;
    --row-grey: #c9cbc8;
    --row-red: #f20f0f;
    --rule: #3a5a45;
  }
  * { box-sizing: border-box; margin: 0; padding: 0; }
  html, body { width: 1200px; height: 1200px; overflow: hidden; background: var(--page-bg); }
  .flyer {
    position: absolute; left: 190px; top: 20px;
    width: 880px; height: 1246px;
    transform: scale(0.931); transform-origin: top left;
    background: linear-gradient(#ffffff, #f4f6f4);
    box-shadow: 0 6px 20px rgba(0,0,0,.25);
    font-family: 'Lato', sans-serif; color: var(--ink);
    overflow: hidden;
  }
  .hero-photo {
    position: absolute; left: 0; top: 0; width: 880px; height: 560px;
    background: linear-gradient(160deg, #2f6fc4 0%, #6ea7e6 45%, #b9d3ea 70%, #5d7f4a 100%);
  }
  .hero-waves { position: absolute; left: 0; top: 380px; width: 880px; height: 230px; }
  .club-badge {
    position: absolute; left: 115px; top: 358px; width: 184px; height: 184px;
    border-radius: 50%; background: var(--paper);
    border: 3px solid var(--green-dark);
    display: flex; align-items: center; justify-content: center; text-align: center;
    font-weight: 700; font-size: 22px; line-height: 1.2; color: var(--green-dark);
    padding: 20px;
  }
  .intro { position: absolute; left: 52px; top: 645px; width: 345px; font-size: 14px; line-height: 18px; text-align: justify; }
  .rule { position: absolute; height: 1px; background: var(--rule); }
  .age { position: absolute; left: 52px; top: 744px; font-size: 22px; color: var(--green-dark); }
  .age b { font-family: 'Bebas Neue', sans-serif; font-weight: 400; font-size: 24px; }
  .divider-v { position: absolute; left: 422px; top: 605px; width: 1px; height: 175px; background: #d3d8d4; }
  .event-title {
    position: absolute; left: 432px; top: 640px; width: 406px;
    font-family: 'Bebas Neue', sans-serif; font-weight: 400; font-size: 38px; line-height: 46px;
    color: var(--green-dark); text-align: center; letter-spacing: .2px;
  }
  .event-title span { display: block; white-space: nowrap; }
  .event-dates { position: absolute; left: 440px; top: 744px; width: 390px; text-align: center; font-size: 21px; color: var(--green-dark); }
  .program-heading { position: absolute; left: 0; top: 804px; width: 880px; text-align: center; font-size: 19px; font-weight: 700; color: var(--green-dark); }
  .schedule {
    position: absolute; left: 55px; top: 838px; width: 771px;
    border: 1.5px solid var(--rule); border-radius: 14px; overflow: hidden;
    box-shadow: 0 6px 10px rgba(0,0,0,.15);
  }
  .schedule-row { position: relative; height: 43.5px; border-bottom: 1.5px solid var(--rule); background: var(--paper); }
  .schedule-row.is-shaded { background: var(--row-grey); }
  .schedule-row.is-leisure { background: var(--row-red); color: #fff; }
  .day { position: absolute; left: 72px; top: 9px; font-size: 16px; font-weight: 700; color: var(--green-dark); }
  .day small { display: block; font-size: 13px; font-weight: 400; margin-top: 1px; }
  .day.has-note { top: 3px; }
  .date { position: absolute; left: 297px; top: 12px; font-size: 16px; color: var(--green-dark); }
  .venue { position: absolute; left: 478px; top: 4px; font-size: 13px; line-height: 17px; color: var(--green-dark); }
  .venue b { font-weight: 700; }
  .is-leisure .day, .is-leisure .date, .is-leisure .venue { color: #fff; }
  .is-leisure .venue { top: 11px; font-size: 16px; font-weight: 700; }
  .schedule-footer { height: 38px; background: var(--row-grey); text-align: center; font-size: 13px; font-weight: 700; line-height: 38px; color: var(--green-dark); padding-right: 90px; }
  .contact-band { position: absolute; left: 0; top: 1173px; width: 880px; height: 73px; background: var(--green); color: #fff; font-size: 14px; }
  .contact-item { position: absolute; display: flex; align-items: center; gap: 10px; }
  .notice-ball {
    position: absolute; left: 705px; top: 1083px; width: 144px; height: 144px; border-radius: 50%;
    background: radial-gradient(circle at 40% 35%, #ffffff 40%, #dfe3df 100%);
    border: 4px solid var(--green-dark);
    box-shadow: 0 4px 10px rgba(0,0,0,.3);
    display: flex; align-items: center; justify-content: center; text-align: center;
    font-family: 'Bebas Neue', sans-serif; font-size: 26px; line-height: 28px; color: var(--green-mid);
  }
</style>
</head>
<body>
<main class="flyer">
  <div class="hero-photo" role="img" aria-label="Photo of a smiling senior couple holding golf clubs under palm trees and blue sky"></div>
  <svg class="hero-waves" viewBox="0 0 880 230" preserveAspectRatio="none" aria-hidden="true">
    <path d="M0 100 C120 60 260 90 380 150 C470 195 560 200 640 180 C740 150 820 120 880 130 L880 230 L0 230 Z" fill="#b9c62e"/>
    <path d="M0 160 C150 180 320 220 470 205 C620 190 740 150 880 155 L880 230 L0 230 Z" fill="#1f7a3f"/>
    <path d="M0 175 C160 200 330 235 480 220 C620 206 740 170 880 170" stroke="#ffffff" stroke-width="3" fill="none"/>
    <path d="M380 215 C540 200 700 160 880 140 L880 230 L380 230 Z" fill="#2a8f4e" opacity=".9"/>
    <path d="M0 230 L0 195 C200 225 360 240 520 230 Z" fill="#0d4a25"/>
    <rect x="0" y="222" width="880" height="8" fill="#ffffff"/>
  </svg>
  <div class="club-badge">Brindle Wexmoor Golf Club</div>

  <p class="intro">We invite our fellow Veteran Ladies and Gentlemen to play a unique 54 hole stableford event at three fantastic Golf Courses, and finish the week at Brindle Golf club with a 2BBB Medley</p>
  <div class="rule" style="left:52px;top:738px;width:345px"></div>
  <p class="age"><b>AGE</b> : Over 55 years of age</p>

  <div class="divider-v"></div>

  <h1 class="event-title"><span>Silver reed Harbour</span><span>Seniors Fairway Festival 2017</span></h1>
  <div class="rule" style="left:440px;top:738px;width:388px"></div>
  <p class="event-dates">16th October to 20th&nbsp; October</p>

  <h2 class="program-heading">SILVER REED HARBOUR SENIORS’ FAIRWAY FESTIVAL PROGRAM</h2>

  <section class="schedule">
    <div class="schedule-row is-shaded"><span class="day">SUNDAY</span><span class="date">15 October</span><span class="venue"><b>Brindle Golf Club</b><br>Registrations: 4.00pm - 6.00pm</span></div>
    <div class="schedule-row"><span class="day">MONDAY</span><span class="date">16 October</span><span class="venue"><b>Wexmoor Golf Course Par 72</b><br>Stableford - 1st Round Championships</span></div>
    <div class="schedule-row is-shaded"><span class="day has-note">TUESDAY<small>RVGA Trophy Day</small></span><span class="date">17 October</span><span class="venue"><b>Calloway Ridge Golf Course Par 71</b><br>Stableford - 2nd Round Championships</span></div>
    <div class="schedule-row is-leisure"><span class="day">WEDNESDAY</span><span class="date">18 October</span><span class="venue">LEISURE</span></div>
    <div class="schedule-row is-shaded"><span class="day">THURSDAY</span><span class="date">19 October</span><span class="venue"><b>Ashgrove Golf Course Par 72</b><br>Stableford - Round 3 Championships</span></div>
    <div class="schedule-row"><span class="day">FRIDAY</span><span class="date">20 October</span><span class="venue"><b>Brindle Golf Course Par 66</b><br>18 Hole 2BBB Medley Stableford</span></div>
    <div class="schedule-footer">Brindle Golf Club - PRESENTATION DINNER DANCE &nbsp;-7.00 pm for 7.30 pm</div>
  </section>

  <footer class="contact-band">
    <span class="contact-item" style="left:76px;top:15px">For entry form and details:</span>
    <span class="contact-item" style="left:76px;top:38px">
      <svg width="12" height="15" viewBox="0 0 12 15" aria-hidden="true"><circle cx="6" cy="4" r="3.5" fill="#e6e34a"/><path d="M1 15 L2 9 Q6 6 10 9 L11 15 Z" fill="#e6e34a"/></svg>Brindle Proshop</span>
    <span class="contact-item" style="left:398px;top:15px">
      <svg width="16" height="12" viewBox="0 0 16 12" aria-hidden="true"><rect x="0" y="0" width="16" height="12" rx="2" fill="#e6e34a"/><rect x="3" y="3" width="10" height="6" fill="#2a8f4e"/></svg>02 63918204</span>
    <span class="contact-item" style="left:398px;top:38px">
      <svg width="16" height="12" viewBox="0 0 16 12" aria-hidden="true"><rect width="16" height="12" rx="1.5" fill="#e6e34a"/><path d="M1 1 L8 7 L15 1" stroke="#2a8f4e" stroke-width="1.5" fill="none"/></svg>admin@brindlewexmoorgolf.com.au</span>
  </footer>

  <div class="notice-ball">Please<br>put me on your<br>notice board</div>
</main>
</body>
</html>
```